Brackenfield Partners Exit Plan business consultant web site

This website is for a consulting business that helps other businesses with exit plans. Essentially, assists them with the sale of their business. This website should be very professional, almost with a wall street look. I would like a very attractive image on the homepage. Perhaps something that denotes success. Perhaps a picture of palm trees and a beach? I will leave it to you for interpretation.

Across the screen I would like the words "Does your business have an exit plan?"

Below that it should read the following:
Let us help you with a completely impartial, no obligation assessment (button with link to the contact page)

Also, please use logo in a prominent place on the website so it's easily seen.

Target Market(s)

Males 40+

Coding

Coded - Design and coding required

Number of Pages Required

5+ page

Colors

Designer to choose colors to be used in the design.

Requirements
Must have
• The tabs for the homepage on the top should be:
• 1. About us
• 2. Services
• 3. Industries
• 4. Our success
• 5. Contact
Nice to have
• Clean, professional image.
• Please put FB, Twitter, Linked In - logos at bottom.
• Here are two examples of a website to give you an idea:
• https://journal.corvanteriq.com/library/why-every-business-owner-should-have-an-exit-plan
Should not have
• nothing whimsical or cartoon like

```html
<!DOCTYPE html>
<html lang="en">
<head>
<meta charset="utf-8">
<title>Brackenfield Partners — Exit Planning Consultants</title>
<link href="https://fonts.googleapis.com/css2?family=Poppins:wght@300;400;500;600;700&family=Montserrat:wght@500;600;700&display=swap" rel="stylesheet">
<style>
:root{
  --ink:#1b1b1b;
  --text:#6f6f6f;
  --muted:#9a9a9a;
  --accent:#d9541c;
  --accent-2:#e0672b;
  --light:#f2f2f2;
  --line:#e4e4e4;
  --footer:#0e0e0e;
  --white:#ffffff;
}
*{box-sizing:border-box;margin:0;padding:0}
html,body{width:1200px;height:3458px;overflow:hidden}
body{font-family:"Poppins",sans-serif;color:var(--ink);background:var(--white);position:relative}
a{color:inherit;text-decoration:none}

/* Header */
.site-header{position:absolute;top:0;left:0;width:1200px;height:100px;background:var(--white)}
.brand{position:absolute;left:235px;top:30px;display:flex;align-items:center;gap:10px}
.brand-square{width:34px;height:34px;background:var(--ink)}
.brand-name{font-family:"Poppins",sans-serif;font-weight:500;font-size:17px;color:var(--ink);letter-spacing:.5px}
.main-nav{position:absolute;top:47px;left:568px;display:flex;font-family:"Montserrat",sans-serif;font-weight:600;font-size:10.5px;color:var(--ink);letter-spacing:.3px}
.main-nav a{margin-right:30px}
.main-nav .caret{font-size:8px;margin-left:3px;color:var(--muted)}

/* Hero */
.hero{position:absolute;top:100px;left:0;width:1200px;height:376px;border:2px solid #c9c9c9;overflow:hidden}
.hero-image{position:absolute;inset:0;background:
  radial-gradient(ellipse 260px 180px at 30% 2%,rgba(255,255,255,.75),rgba(255,255,255,0) 70%),
  radial-gradient(ellipse 520px 200px at 85% 38%,rgba(30,30,30,.75),rgba(30,30,30,0) 70%),
  radial-gradient(ellipse 180px 60px at 88% 92%,rgba(35,35,35,.8),rgba(35,35,35,0) 70%),
  linear-gradient(180deg,#9a9a9a 0%,#7e7e7e 30%,#6a6a6a 46%,#5b5b5b 52%,#8c8c8c 56%,#bdbdbd 64%,#a3a3a3 74%,#8a8a8a 86%,#6f6f6f 100%)}
.hero-shade{position:absolute;inset:0;background:rgba(0,0,0,.18)}
.hero-inner{position:absolute;inset:5px;border:1px solid rgba(255,255,255,.55)}
.hero-copy{position:absolute;top:138px;left:0;width:100%;text-align:center;color:var(--white)}
.hero-copy h1{font-family:"Montserrat",sans-serif;font-weight:700;font-size:18px;letter-spacing:.2px}
.hero-copy p{font-size:15.5px;font-weight:400;line-height:22px;width:370px;margin:4px auto 0}
.btn-solid{display:inline-block;background:var(--accent);color:var(--white);font-family:"Montserrat",sans-serif;font-weight:600;font-size:10px;padding:0 16px;height:28px;line-height:28px;margin-top:12px}

/* Shared section head */
.section{position:absolute;left:0;width:1200px}
.section-head{position:absolute;top:55px;left:0;width:100%;text-align:center}
.section-mark{width:32px;height:34px;background:var(--ink);margin:0 auto;border:3px double var(--white);outline:1px solid var(--ink)}
.section-head h2{font-weight:400;font-size:27px;letter-spacing:1.6px;margin-top:9px;color:var(--ink)}
.section-head p{font-size:10px;line-height:15px;color:var(--text);margin-top:6px}
.section-head .rule{width:40px;height:2px;background:var(--accent);margin:14px auto 0}

/* About */
.about{top:476px;height:561px;background:linear-gradient(120deg,#f7f7f7 0%,#fff 45%,#fff 100%)}
.about-frame{position:absolute;left:267px;top:261px;width:355px;height:245px;border:4px solid var(--ink)}
.about-photo{position:absolute;left:235px;top:226px;width:355px;height:251px;background:linear-gradient(135deg,#c9d3dc,#8a9bab 45%,#e9edf0);border:4px solid var(--white)}
.about-text{position:absolute;left:652px;top:240px;width:314px;font-size:9.3px;line-height:15px;color:#3a3a3a;text-align:justify}
.about-text p+p{margin-top:15px}
.about-actions{position:absolute;left:652px;top:444px;display:flex;align-items:center;gap:17px}
.btn-pill{background:var(--accent);color:var(--white);font-family:"Montserrat",sans-serif;font-weight:700;font-size:7.5px;width:86px;height:29px;line-height:29px;text-align:center;border-radius:15px}
.watch{display:flex;align-items:center;gap:8px;font-family:"Montserrat",sans-serif;font-weight:700;font-size:9.5px;letter-spacing:.4px}

/* Services */
.services{top:1037px;height:678px;background:var(--light)}
.service-card{position:absolute;width:231px;height:187px;overflow:hidden}
.service-card .photo{position:absolute;inset:0}
.service-card .shade{position:absolute;left:0;right:0;bottom:0;height:70px;background:linear-gradient(180deg,rgba(0,0,0,0),rgba(0,0,0,.75))}
.service-card h3{position:absolute;left:17px;bottom:17px;color:var(--white);font-weight:600;font-size:13px;letter-spacing:1px}
.service-card .go{position:absolute;right:0;bottom:0;width:44px;height:44px;background:var(--accent);display:flex;align-items:center;justify-content:center}

/* Testimonials */
.testimonials{top:1715px;height:534px;background:var(--white)}
.quote-card{position:absolute;top:220px;width:233px;height:184px;border:1px solid var(--line);border-radius:3px;padding:18px 21px}
.quote-card .top{display:flex;justify-content:space-between;align-items:center}
.stars{color:#f5a623;font-size:13px;letter-spacing:4px}
.quote-card p{font-size:9px;line-height:15px;color:var(--text);margin-top:14px}
.person{display:flex;align-items:center;gap:12px;margin-top:14px}
.avatar{width:46px;height:46px;border-radius:50%;background:linear-gradient(135deg,#b9a89a,#6f6358)}
.person strong{display:block;font-family:"Montserrat",sans-serif;font-size:9.5px;font-weight:700}
.person span{font-size:9px;color:var(--text)}
.slider-nav{position:absolute;top:449px;left:547px;display:flex;align-items:center;gap:10px}
.arrow-btn{width:25px;height:25px;border-radius:50%;border:1px solid #d6d6d6;display:flex;align-items:center;justify-content:center;font-size:10px;color:#777}
.dots{display:flex;gap:6px;margin:0 4px}
.dots i{width:5px;height:5px;border-radius:50%;background:#cfcfcf}
.dots i.on{background:var(--accent)}

/* Funfacts */
.funfacts{top:2249px;height:357px;background:linear-gradient(90deg,#20262d,#2b333c 50%,#1c2127);color:var(--white)}
.funfacts .section-mark{background:transparent;border:3px double var(--white);outline:1px solid var(--white)}
.funfacts h2{font-weight:400;font-size:25px;letter-spacing:1.8px;text-align:center;position:absolute;top:104px;width:100%}
.fact{position:absolute;top:190px;width:200px;text-align:center}
.fact .num{font-weight:700;font-size:37px;line-height:44px;margin-top:6px;letter-spacing:1px}
.fact .label{font-weight:500;font-size:14px;letter-spacing:1px}

/* News */
.news{top:2606px;height:541px;background:var(--white)}
.news-card{position:absolute;top:216px;width:232px}
.news-card .photo{height:135px}
.news-card h3{font-size:11.2px;font-weight:700;line-height:15px;margin-top:16px}
.news-card p{font-size:9.3px;line-height:15px;color:var(--text);margin-top:8px}
.news-card .meta{display:flex;align-items:center;gap:8px;margin-top:22px;font-size:9px;color:var(--muted)}
.news-card .sep{width:1px;height:9px;background:#ccc}

/* Footer */
.site-footer{position:absolute;top:3147px;left:0;width:1200px;height:311px;background:radial-gradient(ellipse at 20% 30%,#1d1d1d,var(--footer) 60%);color:var(--white)}
.footer-brand{position:absolute;left:232px;top:48px;width:240px;text-align:center}
.footer-brand .brand-square{width:46px;height:46px;background:var(--white);margin:0 auto}
.footer-brand .brand-name{color:var(--white);display:block;margin-top:10px;font-size:16px}
.footer-brand p{font-size:8.7px;line-height:15px;margin-top:10px}
.footer-col{position:absolute;top:60px}
.footer-col h4{font-family:"Montserrat",sans-serif;font-weight:700;font-size:10px;letter-spacing:.4px}
.quick-links li{list-style:none;font-size:8.7px;margin-top:11px;display:flex;align-items:center;gap:9px}
.quick-links li::before{content:"";width:9px;height:1px;background:var(--white)}
.quick-links li:first-child{margin-top:22px}
.contact-row{display:flex;gap:12px;font-size:8.7px;line-height:14px;margin-top:12px;align-items:flex-start}
.contact-row:first-of-type{margin-top:18px}
.contact-icon{width:20px;height:20px;background:var(--accent);border-radius:2px;flex:none;display:flex;align-items:center;justify-content:center}
.newsletter p{font-size:8.7px;line-height:15px;margin-top:18px;width:170px}
.subscribe{display:flex;margin-top:12px;width:169px;height:30px}
.subscribe .field{flex:1;background:var(--white);color:var(--muted);font-size:8.5px;display:flex;align-items:center;padding-left:10px;gap:6px}
.subscribe .send{width:38px;background:var(--accent);display:flex;align-items:center;justify-content:center}
.socials{display:flex;gap:8px;margin-top:14px}
.socials a{width:24px;height:24px;border:1px solid var(--white);border-radius:50%;display:flex;align-items:center;justify-content:center}
.copyright{position:absolute;top:3402px;left:0;width:1200px;text-align:center;font-size:8.7px;color:var(--white)}
.copyright em{font-style:normal;color:var(--accent-2)}
</style>
</head>
<body>

<header class="site-header">
  <a class="brand" href="#"><span class="brand-square"></span><span class="brand-name">Brackenfield Partners</span></a>
  <nav class="main-nav">
    <a href="#">ABOUT US</a>
    <a href="#">SERVICES<span class="caret">&#8964;</span></a>
    <a href="#">INDUSTRIES</a>
    <a href="#">OUR SUCCESS</a>
    <a href="#">CONTACT</a>
  </nav>
</header>

<section class="hero">
  <div class="hero-image" role="img" aria-label="Black and white photograph of a tropical beach at sunrise, with palm trees on the right, sun rays in the sky, calm sea and rocks on the sand"></div>
  <div class="hero-shade"></div>
  <div class="hero-inner"></div>
  <div class="hero-copy">
    <h1>DOES YOUR BUSINESS HAVE AN EXIT PLAN?</h1>
    <p>Let us help you with a completely impartial, no obligation assessment</p>
    <a class="btn-solid" href="#">CONTACT US</a>
  </div>
</section>

<section class="section about">
  <div class="section-head">
    <div class="section-mark"></div>
    <h2>About Us</h2>
    <p>Curabitur et iaculis ex. Maecenas et tortor in ipsum fermentum porta.<br>Maecenas sapien urna, euismod at congue ac, elementum sed odio.</p>
    <div class="rule"></div>
  </div>
  <div class="about-frame"></div>
  <div class="about-photo" role="img" aria-label="Photograph of three business colleagues reviewing a document together"></div>
  <div class="about-text">
    <p>Lorem ipsum dolor sit amet, consectetur adipiscing elit. Etiam efficitur dolor massa, ac molestie sem lacinia vel. Donec laoreet porta diam at fringilla. Praesent lorem libero, condimentum sed lacinia iaculis, feugiat id massa. Mauris a placerat purus, eget iaculis nunc. Fusce molestie, purus non elementum pulvinar, ligula sapien facilisis nibh, rhoncus porta mauris lacus ut leo. Nullam aliquet ante et elit lacinia porttitor. Vestibulum fringilla lacinia imperdiet.</p>
    <p>Fusce vitae tincidunt dolor. Vivamus sed nunc ut nunc fringilla sollicitudin. Fusce sodales massa sed sapien bibendum dictum ac sit amet risus. Nulla accumsan urna eu arcu ultrices imperdiet. Sed turpis urna, auctor eu sodales quis, egestas nec elit.</p>
  </div>
  <div class="about-actions">
    <a class="btn-pill" href="#">READ MORE</a>
    <span class="watch">
      <svg width="26" height="26" viewBox="0 0 26 26"><circle cx="13" cy="13" r="11.5" fill="none" stroke="#1b1b1b" stroke-width="2.4"/><path d="M10.5 8.5 L17.5 13 L10.5 17.5Z" fill="#1b1b1b"/></svg>
      WATCH VIDEO
    </span>
  </div>
</section>

<section class="section services">
  <div class="section-head">
    <div class="section-mark"></div>
    <h2>Our Services</h2>
    <p>Curabitur et iaculis ex. Maecenas et tortor in ipsum fermentum porta.<br>Maecenas sapien urna, euismod at congue ac, elementum sed odio.</p>
    <div class="rule"></div>
  </div>

  <article class="service-card" style="left:235px;top:227px">
    <div class="photo" role="img" aria-label="Photograph of a team gathered around a laptop" style="background:linear-gradient(135deg,#8c7a6b,#c7b3a3 50%,#6e5e52)"></div>
    <div class="shade"></div><h3>Financial Analysis</h3>
    <span class="go"><svg width="14" height="12" viewBox="0 0 14 12"><path d="M1 6H12M7.5 1.5L12 6L7.5 10.5" fill="none" stroke="#fff" stroke-width="1.5"/></svg></span>
  </article>
  <article class="service-card" style="left:484px;top:227px">
    <div class="photo" role="img" aria-label="Photograph of colleagues working together in a bright office" style="background:linear-gradient(135deg,#9fb0bf,#5f6f7d 55%,#c6d0d8)"></div>
    <div class="shade"></div><h3>Business Growth</h3>
    <span class="go"><svg width="14" height="12" viewBox="0 0 14 12"><path d="M1 6H12M7.5 1.5L12 6L7.5 10.5" fill="none" stroke="#fff" stroke-width="1.5"/></svg></span>
  </article>
  <article class="service-card" style="left:734px;top:227px">
    <div class="photo" role="img" aria-label="Photograph of a meeting in a modern lounge" style="background:linear-gradient(135deg,#b9b2ab,#7d6f66 50%,#c4564a)"></div>
    <div class="shade"></div><h3>Success Report</h3>
    <span class="go"><svg width="14" height="12" viewBox="0 0 14 12"><path d="M1 6H12M7.5 1.5L12 6L7.5 10.5" fill="none" stroke="#fff" stroke-width="1.5"/></svg></span>
  </article>
  <article class="service-card" style="left:235px;top:433px">
    <div class="photo" role="img" aria-label="Photograph of executives around a boardroom table" style="background:linear-gradient(135deg,#a8b3bc,#48525c 55%,#8e9aa3)"></div>
    <div class="shade"></div><h3>Marketing Plan</h3>
    <span class="go"><svg width="14" height="12" viewBox="0 0 14 12"><path d="M1 6H12M7.5 1.5L12 6L7.5 10.5" fill="none" stroke="#fff" stroke-width="1.5"/></svg></span>
  </article>
  <article class="service-card" style="left:484px;top:433px">
    <div class="photo" role="img" aria-label="Photograph of a smiling businesswoman with a team behind her" style="background:linear-gradient(135deg,#d6d8da,#9ea4a9 50%,#6b7177)"></div>
    <div class="shade"></div><h3>Global Business</h3>
    <span class="go"><svg width="14" height="12" viewBox="0 0 14 12"><path d="M1 6H12M7.5 1.5L12 6L7.5 10.5" fill="none" stroke="#fff" stroke-width="1.5"/></svg></span>
  </article>
  <article class="service-card" style="left:734px;top:433px">
    <div class="photo" role="img" aria-label="Photograph of a confident businesswoman in an office" style="background:linear-gradient(135deg,#7c8791,#b7bfc6 55%,#e0e3e6)"></div>
    <div class="shade"></div><h3>Risk Management</h3>
    <span class="go"><svg width="14" height="12" viewBox="0 0 14 12"><path d="M1 6H12M7.5 1.5L12 6L7.5 10.5" fill="none" stroke="#fff" stroke-width="1.5"/></svg></span>
  </article>
</section>

<section class="section testimonials">
  <div class="section-head">
    <div class="section-mark"></div>
    <h2>Words from our Clients</h2>
    <p>Curabitur et iaculis ex. Maecenas et tortor in ipsum fermentum porta.<br>Maecenas sapien urna, euismod at congue ac, elementum sed odio.</p>
    <div class="rule"></div>
  </div>

  <article class="quote-card" style="left:234px">
    <div class="top"><svg width="14" height="10" viewBox="0 0 14 10"><path d="M0 10V5Q0 0 5 0V2Q2 2 2 5H5V10ZM8 10V5Q8 0 13 0V2Q10 2 10 5H13V10Z" fill="#5aa9e6"/></svg><span class="stars">★★★★★</span></div>
    <p>Lorem ipsum dolor sit amet, consectetur adipiscing elit. Quisque iaculis elementum eleifend. Cras malesuada vitae enim id imperdiet. Vestibulum vestibulum egestas.</p>
    <div class="person"><span class="avatar" role="img" aria-label="Client portrait"></span><div><strong>MARTIN KESSEL</strong><span>Client</span></div></div>
  </article>
  <article class="quote-card" style="left:484px">
    <div class="top"><svg width="14" height="10" viewBox="0 0 14 10"><path d="M0 10V5Q0 0 5 0V2Q2 2 2 5H5V10ZM8 10V5Q8 0 13 0V2Q10 2 10 5H13V10Z" fill="#5aa9e6"/></svg><span class="stars">★★★★★</span></div>
    <p>Lorem ipsum dolor sit amet, consectetur adipiscing elit. Quisque iaculis elementum eleifend. Cras malesuada vitae enim id imperdiet. Vestibulum vestibulum egestas.</p>
    <div class="person"><span class="avatar" role="img" aria-label="Client portrait" style="background:linear-gradient(135deg,#d7d7d7,#8e8e8e)"></span><div><strong>MARTIN KESSEL</strong><span>Client</span></div></div>
  </article>
  <article class="quote-card" style="left:734px">
    <div class="top"><svg width="14" height="10" viewBox="0 0 14 10"><path d="M0 10V5Q0 0 5 0V2Q2 2 2 5H5V10ZM8 10V5Q8 0 13 0V2Q10 2 10 5H13V10Z" fill="#5aa9e6"/></svg><span class="stars">★★★★★</span></div>
    <p>Lorem ipsum dolor sit amet, consectetur adipiscing elit. Quisque iaculis elementum eleifend. Cras malesuada vitae enim id imperdiet. Vestibulum vestibulum egestas.</p>
    <div class="person"><span class="avatar" role="img" aria-label="Client portrait" style="background:linear-gradient(135deg,#a27b55,#4c3a2c)"></span><div><strong>MARTIN KESSEL</strong><span>Client</span></div></div>
  </article>

  <div class="slider-nav">
    <span class="arrow-btn">&#8249;</span>
    <span class="dots"><i></i><i class="on"></i><i></i></span>
    <span class="arrow-btn">&#8250;</span>
  </div>
</section>

<section class="section funfacts" aria-label="Company figures over a dark photograph of a business meeting">
  <div class="section-head" style="top:56px"><div class="section-mark"></div></div>
  <h2>See Our Awesome Funfacts</h2>

  <div class="fact" style="left:218px">
    <svg width="40" height="36" viewBox="0 0 40 36"><rect x="2" y="9" width="36" height="25" rx="3" fill="#fff"/><rect x="14" y="2" width="12" height="8" rx="2" fill="none" stroke="#fff" stroke-width="3"/><rect x="11" y="9" width="3" height="25" fill="#262d35"/><rect x="26" y="9" width="3" height="25" fill="#262d35"/></svg>
    <div class="num">1224</div><div class="label">Cases Completed</div>
  </div>
  <div class="fact" style="left:405px">
    <svg width="40" height="36" viewBox="0 0 40 36"><circle cx="20" cy="11" r="8" fill="none" stroke="#fff" stroke-width="3"/><path d="M5 34Q5 21 20 21Q35 21 35 34Z" fill="none" stroke="#fff" stroke-width="3"/></svg>
    <div class="num">32</div><div class="label">Team Member</div>
  </div>
  <div class="fact" style="left:592px">
    <svg width="40" height="36" viewBox="0 0 40 36"><circle cx="20" cy="18" r="15" fill="none" stroke="#fff" stroke-width="5"/><circle cx="20" cy="18" r="6" fill="none" stroke="#fff" stroke-width="3"/><path d="M9 7L15 13M31 7L25 13M9 29L15 23M31 29L25 23" stroke="#262d35" stroke-width="4"/></svg>
    <div class="num">15</div><div class="label">Years Experience</div>
  </div>
  <div class="fact" style="left:779px">
    <svg width="40" height="36" viewBox="0 0 40 36"><path d="M5 16H11V34H5Z M14 16L21 4Q25 4 24 10L23 15H33Q37 15 36 19L33 31Q32 34 29 34H14Z" fill="none" stroke="#fff" stroke-width="2.6" stroke-linejoin="round"/></svg>
    <div class="num">1475</div><div class="label">Satisfied Customers</div>
  </div>
</section>

<section class="section news">
  <div class="section-head">
    <div class="section-mark"></div>
    <h2>Latest News</h2>
    <p>Curabitur et iaculis ex. Maecenas et tortor in ipsum fermentum porta.<br>Maecenas sapien urna, euismod at congue ac, elementum sed odio.</p>
    <div class="rule"></div>
  </div>

  <article class="news-card" style="left:234px">
    <div class="photo" role="img" aria-label="Photograph of hands reviewing paperwork beside a laptop" style="background:linear-gradient(135deg,#c9d3d6,#7d8c92 50%,#e7ecee)"></div>
    <h3>Lorem ipsum dolor sit amet, con sectetur adipiscing elit.</h3>
    <p>Fusce vitae tincidunt dolor. Vivamus sed nunc ut nunc fringilla sollicitudin. Fusce sodales massa sed sapien bibendum dictum ac sit amet risus.</p>
    <div class="meta"><svg width="9" height="9" viewBox="0 0 9 9"><circle cx="4.5" cy="2.5" r="2.2" fill="#1b1b1b"/><path d="M0.5 9Q0.5 5 4.5 5Q8.5 5 8.5 9Z" fill="#1b1b1b"/></svg>admin<span class="sep"></span><svg width="11" height="9" viewBox="0 0 11 9"><path d="M1 1H10V6H4L1.5 8.5V6H1Z" fill="#1b1b1b"/></svg>comments:0</div>
  </article>
  <article class="news-card" style="left:484px">
    <div class="photo" role="img" aria-label="Photograph of a laptop showing a financial dashboard" style="background:linear-gradient(135deg,#5b4a3b,#2d3338 50%,#8fa5b2)"></div>
    <h3>Lorem ipsum dolor sit amet, con sectetur adipiscing elit.</h3>
    <p>Fusce vitae tincidunt dolor. Vivamus sed nunc ut nunc fringilla sollicitudin. Fusce sodales massa sed sapien bibendum dictum ac sit amet risus.</p>
    <div class="meta"><svg width="9" height="9" viewBox="0 0 9 9"><circle cx="4.5" cy="2.5" r="2.2" fill="#1b1b1b"/><path d="M0.5 9Q0.5 5 4.5 5Q8.5 5 8.5 9Z" fill="#1b1b1b"/></svg>admin<span class="sep"></span><svg width="11" height="9" viewBox="0 0 11 9"><path d="M1 1H10V6H4L1.5 8.5V6H1Z" fill="#1b1b1b"/></svg>comments:0</div>
  </article>
  <article class="news-card" style="left:734px">
    <div class="photo" role="img" aria-label="Photograph of a person working at a laptop with a coffee cup" style="background:linear-gradient(135deg,#c7b4a6,#4d4a4a 50%,#9aa6b5)"></div>
    <h3>Lorem ipsum dolor sit amet, con sectetur adipiscing elit.</h3>
    <p>Fusce vitae tincidunt dolor. Vivamus sed nunc ut nunc fringilla sollicitudin. Fusce sodales massa sed sapien bibendum dictum ac sit amet risus.</p>
    <div class="meta"><svg width="9" height="9" viewBox="0 0 9 9"><circle cx="4.5" cy="2.5" r="2.2" fill="#1b1b1b"/><path d="M0.5 9Q0.5 5 4.5 5Q8.5 5 8.5 9Z" fill="#1b1b1b"/></svg>admin<span class="sep"></span><svg width="11" height="9" viewBox="0 0 11 9"><path d="M1 1H10V6H4L1.5 8.5V6H1Z" fill="#1b1b1b"/></svg>comments:0</div>
  </article>
</section>

<footer class="site-footer">
  <div class="footer-brand">
    <div class="brand-square"></div>
    <span class="brand-name">Brackenfield Partners</span>
    <p>Lorem ipsum dolor sit amet, consectetur adipiscing elit. Etiam efficitur dolor massa, ac molestie sem lacinia vel. Donec laoreet porta diam at fringilla.</p>
  </div>

  <div class="footer-col" style="left:497px">
    <h4>QUICK LINKS</h4>
    <ul class="quick-links">
      <li>About Us</li><li>Services</li><li>Industries</li><li>Our Success</li><li>Contact</li>
    </ul>
  </div>

  <div class="footer-col" style="left:604px">
    <h4>GET IN TOUCH</h4>
    <div class="contact-row"><span class="contact-icon"><svg width="10" height="10" viewBox="0 0 10 10"><path d="M2 0.5L4 3L3 4Q4 6 6 7L7 6L9.5 8L8.5 9.5Q1 9 0.5 1.5Z" fill="#fff"/></svg></span><span style="padding-top:3px">(000) 123 4567</span></div>
    <div class="contact-row"><span class="contact-icon"><svg width="11" height="8" viewBox="0 0 11 8"><rect x=".5" y=".5" width="10" height="7" fill="#fff"/><path d="M.5 .5L5.5 4.5L10.5 .5" fill="none" stroke="#d9541c"/></svg></span><span style="padding-top:3px">info@brackenfieldpartners.com</span></div>
    <div class="contact-row"><span class="contact-icon"><svg width="9" height="11" viewBox="0 0 9 11"><path d="M4.5 10.5Q0.5 6 0.5 4A4 4 0 0 1 8.5 4Q8.5 6 4.5 10.5Z" fill="#fff"/><circle cx="4.5" cy="4" r="1.5" fill="#d9541c"/></svg></span><span style="padding-top:3px">123, Street Name, Area Name,<br>City, Zip Code</span></div>
  </div>

  <div class="footer-col newsletter" style="left:797px">
    <h4>NEWSLETTER</h4>
    <p>Enter your email to receive updates and specials</p>
    <div class="subscribe">
      <span class="field"><svg width="10" height="7" viewBox="0 0 10 7"><rect x=".5" y=".5" width="9" height="6" fill="none" stroke="#999"/><path d="M.5 .5L5 4L9.5 .5" fill="none" stroke="#999"/></svg>Email Address</span>
      <span class="send"><svg width="13" height="13" viewBox="0 0 13 13"><path d="M12.5 .5L.5 5.5L5 7L6.5 12.5Z" fill="#fff"/></svg></span>
    </div>
    <div class="socials">
      <a href="#" aria-label="Share"><svg width="11" height="11" viewBox="0 0 11 11"><circle cx="2.2" cy="5.5" r="1.6" fill="#fff"/><circle cx="8.8" cy="2" r="1.6" fill="#fff"/><circle cx="8.8" cy="9" r="1.6" fill="#fff"/><path d="M2.2 5.5L8.8 2M2.2 5.5L8.8 9" stroke="#fff" stroke-width="1"/></svg></a>
      <a href="#" aria-label="Message us"><svg width="11" height="10" viewBox="0 0 11 10"><path d="M1 1H10V7H4.5L2 9.5V7H1Z" fill="none" stroke="#fff" stroke-width="1.2" stroke-linejoin="round"/></svg></a>
      <a href="#" aria-label="Professional network"><svg width="11" height="10" viewBox="0 0 11 10"><rect x=".8" y="3" width="9.4" height="6.2" rx="1" fill="none" stroke="#fff" stroke-width="1.2"/><path d="M3.8 3V1.2H7.2V3" fill="none" stroke="#fff" stroke-width="1.2"/></svg></a>
    </div>
  </div>
</footer>
<div class="copyright">Copyright © 2020 <em>Brackenfield Partners</em>. All Rights Reserved</div>

</body>
</html>
```